Brava Set CEO and Partners Business Card

We need a fresh, fun, simple and clean business card design....we would like a template where we can add a name and title (as well as specific email addresses). We are open to different looks (full logo on one side and a small logo on the company info side, or our logo is in the background but faint on one side but full on the other, or something else cool :-) ). Our colors are in our logo: blue, black and white...however we are not opposed to the use of other colors if it works. We build sets, make props and a host of other things for the film and television industry...our card should reflect creativity, style and professionalism.

A white background would be preferred.

I would like to see an option with Facebook and Instagram icons.

Facebook- facebook.com/bravasetny
Instagram- brava_set

Our website is bravaset-example.com.

Brava Set, Inc.
418 Corvell Avenue, Unit 9
North Hollywood, California 91602
555.210.4873 | tel
555.210.6692 | fax
www.BravaSet-example.com

Sample Name and Title #1:

Peter Halvik
CEO / Co-Owner
555.210.4873 | tel
555.210.6692 | fax
peter@bravaset-example.com
www.BravaSet-example.com

Target Market(s)

Marketing Professionals, Production Designers, Interior Designers, Film Producers, Directors, Art Directors, Event Directors

Industry/Entity Type

Entertainment Industry

Contact Information for Business Card

Peter Halvik
CEO / Co-Owner
555.210.4873 | tel
555.210.6692 | fax
peter@bravaset-example.com
www.BravaSet-example.com

Font styles to use
Sans Serif

Colors
33a6d7
ffffff
1b1b1b

Requirements
Must have
• Logo, All Contact Info, White Background. Symmetry.
Nice to have
• Facebook and Instagram icons with addresses
• Facebook- facebook.com/bravasetny
• Instagram- brava_set

```html
<!DOCTYPE html>
<html lang="en">
<head>
<meta charset="utf-8">
<title>Brava Set — Business Card</title>
<link rel="stylesheet" href="https://fonts.googleapis.com/css2?family=Open+Sans:wght@400;600;800&family=Noto+Serif:wght@700&display=swap">
<style>
  :root {
    --brand-blue: #33a6d7;
    --brand-blue-soft: #7cc6e6;
    --ink: #1b1b1b;
    --paper: #ffffff;
    --stage: #e9ebee;
    --rule: #9aa3a8;
  }
  * { box-sizing: border-box; margin: 0; padding: 0; }
  html, body { width: 1200px; height: 892px; overflow: hidden; }
  body {
    background: var(--stage);
    font-family: "Open Sans", Arial, sans-serif;
    color: var(--ink);
    display: flex;
    flex-direction: column;
    align-items: center;
    justify-content: center;
    gap: 56px;
  }
  .card {
    position: relative;
    width: 620px;
    height: 354px;
    border-radius: 4px;
    overflow: hidden;
    box-shadow: 0 6px 18px rgba(0,0,0,.15);
  }

  /* Back side */
  .card--back { background: var(--brand-blue); color: var(--paper); }
  .back-brand {
    position: absolute; left: 0; right: 0; top: 92px;
    text-align: center;
  }
  .back-brand__name {
    font-weight: 800; font-size: 74px; letter-spacing: 1px; line-height: 1;
  }
  .back-brand__web {
    margin-top: 10px; font-weight: 600; font-size: 17px; letter-spacing: 2px;
  }
  .socials {
    position: absolute; left: 40px; right: 40px; bottom: 46px;
    display: flex; justify-content: space-between; align-items: center;
    font-size: 22px; font-weight: 600;
  }
  .social { display: flex; align-items: center; gap: 14px; }
  .social__mark { width: 28px; height: 28px; background: var(--paper); }
  .social__mark--circle { border-radius: 50%; }

  /* Front side */
  .card--front { background: var(--paper); }
  .decor { position: absolute; display: block; }
  .decor--top { left: 0; top: 0; }
  .decor--bottom { left: 0; bottom: 0; }
  .front-brand {
    position: absolute; left: 300px; top: 96px; width: 290px;
    text-align: center;
    font-weight: 800; font-size: 46px; letter-spacing: .5px; line-height: 1;
    color: var(--ink);
  }
  .contact {
    position: absolute; left: 26px; top: 176px; width: 258px;
    list-style: none; font-size: 11.5px; line-height: 1.35;
  }
  .contact__item {
    display: flex; justify-content: flex-end; align-items: flex-start;
    gap: 10px; margin-bottom: 7px; text-align: right;
  }
  .contact__icon { flex: 0 0 16px; width: 16px; height: 16px; color: var(--brand-blue); }
  .contact__at { color: var(--brand-blue); font-weight: 600; font-size: 14px; line-height: 16px; text-align: center; }
  .divider {
    position: absolute; left: 300px; top: 172px; width: 1px; height: 112px;
    background: var(--rule);
  }
  .person { position: absolute; left: 322px; top: 192px; }
  .person__name {
    font-family: "Noto Serif", Georgia, serif; font-weight: 700;
    font-size: 28px; letter-spacing: 1px; color: var(--ink);
  }
  .person__name-last { color: var(--brand-blue); }
  .person__title { margin-top: 6px; font-size: 15px; color: var(--ink); }
</style>
</head>
<body>

<section class="card card--back" aria-label="Card back">
  <div class="back-brand">
    <div class="back-brand__name">BRAVA SET</div>
    <div class="back-brand__web">www.BravaSet-example.com</div>
  </div>
  <div class="socials">
    <div class="social"><span class="social__mark social__mark--circle"></span><span>brava_set</span></div>
    <div class="social"><span class="social__mark"></span><span>bravasetny</span></div>
  </div>
</section>

<section class="card card--front" aria-label="Card front">
  <svg class="decor decor--top" width="620" height="110" viewBox="0 0 620 110" role="img" aria-label="Sweeping band of blue dot pattern across the top left">
    <defs>
      <linearGradient id="band-top" x1="0" y1="0" x2="1" y2="0">
        <stop offset="0" stop-color="#33a6d7"/>
        <stop offset="1" stop-color="#7cc6e6" stop-opacity=".35"/>
      </linearGradient>
    </defs>
    <path d="M0 0 H400 C330 30 240 60 120 80 C70 88 30 92 0 100 Z" fill="url(#band-top)"/>
  </svg>
  <svg class="decor decor--bottom" width="620" height="110" viewBox="0 0 620 110" role="img" aria-label="Sweeping band of blue dot pattern along the bottom">
    <defs>
      <linearGradient id="band-bottom" x1="0" y1="0" x2="1" y2="0">
        <stop offset="0" stop-color="#7cc6e6" stop-opacity=".35"/>
        <stop offset="1" stop-color="#33a6d7"/>
      </linearGradient>
    </defs>
    <path d="M160 110 C260 70 420 40 620 20 V110 Z" fill="url(#band-bottom)"/>
  </svg>

  <div class="front-brand">BRAVA SET</div>

  <ul class="contact">
    <li class="contact__item"><span>555 210 4873</span>
      <svg class="contact__icon" viewBox="0 0 16 16"><rect x="4" y="1" width="8" height="14" rx="1.5" fill="none" stroke="currentColor" stroke-width="1.4"/><line x1="7" y1="12.5" x2="9" y2="12.5" stroke="currentColor" stroke-width="1.2"/></svg></li>
    <li class="contact__item"><span>555 210 6692</span>
      <svg class="contact__icon" viewBox="0 0 16 16"><rect x="1" y="6" width="14" height="9" rx="1" fill="currentColor"/><rect x="4" y="1" width="8" height="6" fill="none" stroke="currentColor" stroke-width="1.3"/><rect x="9" y="9" width="4" height="1.5" fill="#fff"/><rect x="9" y="11.5" width="4" height="1.5" fill="#fff"/></svg></li>
    <li class="contact__item"><span>peter@bravaset-example.com</span>
      <span class="contact__icon contact__at">@</span></li>
    <li class="contact__item"><span>418 Corvell Avenue,<br>Unit 9 North Hollywood,<br>California 91602</span>
      <svg class="contact__icon" viewBox="0 0 16 16"><path d="M8 1a5 5 0 0 0-5 5c0 4 5 9 5 9s5-5 5-9a5 5 0 0 0-5-5z" fill="currentColor"/><circle cx="8" cy="6" r="1.8" fill="#fff"/></svg></li>
  </ul>

  <div class="divider"></div>

  <div class="person">
    <div class="person__name">Peter <span class="person__name-last">Halvik</span></div>
    <div class="person__title">CEO / Co-Owner</div>
  </div>
</section>

</body>
</html>
```